Roofing & Siding door hanger flyer

-Looking to make door hanger flyer for Pellmont Roofing & Siding
-4.5" wide x 11" tall
-2 sided full colour
-We have started a new website (the content is changing) I have attached photos.
-About us:
-25 year labour warranty's available
-32 years in Calgary
-QCR A+ Member
-NWTG (Prairie Joint Shingle Guild) (logo attached)
-KOV Summit Select (logo attached)
-Owen Brisket (logo attached)
-Slogan "Raised On Care, Proven Through Seasons" 32 years in Calgary
-Sale
-Page 1 & 2 design ideas
We are in your area, contact us today for your Exclusive limited time offer! *discounts apply exclusively to new agreements only
Updates
-Please keep simple, clean & bright
-I really like the bright blue from our new logo (new logo uploaded)
-We specialize in Roofing -Siding-Gutters & full Exterior Renos (like the competitor example uploaded)
-This is the NEW website we are currently working on (not finished) https://mockview.example-draftpad.net/view/1a2b3c4d-5e6f-4a7b-8c9d-0e1f2a3b4c5d-7k2m/?fullscreen
-This is our OLD website https://pellmontshingleworks.com
-For the sale "We are in your area, contact us today for your Exclusive limited time offer" *discounts apply exclusively to new agreements only
-Free Estimates
-our phone# is 403-555-0148
-our website is pellmontshingleworks.com
-keep simple, clean, bright use the "new logo" uploaded. Check out the competitor example uploaded file
-We are in your area, Contact us today for your Exclusive limited time offer! *discounts apply to new agreements only
-FREE ESTIMATES
-Specialized in Roofing /Siding /Gutters Full Exterior Reno's
-We are currently working on a NEW website https://mockview.example-draftpad.net/view/1a2b3c4d-5e6f-4a7b-8c9d-0e1f2a3b4c5d-7k2m/?fullscreen
-Our OLD website https://pellmontshingleworks.com/
-Post old site address on flyer pellmontshingleworks.com
-Phone # 403-555-0148
Target Market(s)
40-55
Industry/Entity Type
Roofing Siding & full Exterior Reno's
Look and feel

```html
<!DOCTYPE html>
<html lang="en">
<head>
<meta charset="utf-8">
<title>Pellmont Roofing &amp; Siding — Door Hanger</title>
<link href="https://fonts.googleapis.com/css2?family=Poppins:ital,wght@0,400;0,500;0,600;0,700;0,800;0,900;1,700;1,800&display=swap" rel="stylesheet">
<style>
:root{
  --stage:#3d3d3d;
  --blue:#0b62b6;
  --blue-deep:#07509a;
  --blue-bright:#1e7fd8;
  --sky:#8fd0f5;
  --sky-pale:#dff1fc;
  --ink:#1d1d1d;
  --text:#3a3a3a;
  --red:#e3141b;
  --white:#ffffff;
}
*{box-sizing:border-box;margin:0;padding:0}
html,body{width:1200px;height:1117px;overflow:hidden}
body{background:var(--stage);font-family:"Poppins",sans-serif;position:relative}
.hanger{position:absolute;top:72px;width:410px;height:976px;background:var(--white);overflow:hidden;box-shadow:0 4px 18px rgba(0,0,0,.35)}
.hanger--front{left:213px}
.hanger--back{left:648px}
.abs{position:absolute}
.headline{position:absolute;top:34px;left:0;width:100%;text-align:center;color:var(--white);font-weight:800;font-size:17px;letter-spacing:-.2px;z-index:3}
.headline em{font-style:normal;color:var(--sky)}
/* brand */
.brand{position:absolute;top:236px;left:0;width:100%;text-align:center}
.brand__est{font-size:13px;letter-spacing:2px;color:var(--ink);font-weight:500}
.brand__name{display:flex;align-items:center;justify-content:center;gap:10px;margin-top:6px;font-size:30px;font-weight:800;color:var(--blue);line-height:1.05}
.brand__mark{width:20px;height:20px;background:var(--blue)}
.brand__sub{font-size:22px;font-weight:800;color:var(--blue);letter-spacing:1px}
/* service blocks */
.service{position:absolute;left:0;width:410px}
.service__bg{position:absolute;left:46px;right:0;top:0;bottom:0;background:linear-gradient(90deg,rgba(255,255,255,1) 0%,var(--sky-pale) 40%,var(--sky) 100%)}
.service__photo{position:absolute;background:linear-gradient(170deg,#b9c7d6 0%,#7d8793 55%,#5e666f 100%)}
.tab{position:absolute;left:33px;top:0;height:40px;background:var(--blue);border-radius:10px 20px 20px 10px;color:var(--white);font-weight:800;font-size:25px;line-height:40px;padding-left:28px;z-index:2;box-shadow:2px 3px 0 rgba(7,80,154,.35)}
.tab::after{content:"";position:absolute;left:0;top:30px;width:14px;height:32px;background:var(--blue-deep);border-radius:0 0 0 10px;z-index:-1}
.checklist{position:absolute;list-style:none;z-index:2}
.checklist li{position:relative;padding-left:20px;font-size:12px;font-weight:500;color:var(--text);line-height:1.3}
.checklist li::before{content:"";position:absolute;left:0;top:3px;width:9px;height:9px;border:1.2px solid var(--blue);border-radius:50%}
.checklist li::after{content:"";position:absolute;left:3.5px;top:5px;width:2px;height:4px;border:solid var(--blue);border-width:0 1.2px 1.2px 0;transform:rotate(45deg)}
.checklist .note{font-weight:400;font-size:11.5px;line-height:1.2}
/* footer */
.footer{position:absolute;left:0;bottom:0;width:410px;height:136px}
.footer svg{position:absolute;inset:0}
.cta{position:absolute;left:64px;top:10px;width:283px;height:33px;background:var(--red);border-radius:17px;color:var(--white);font-weight:800;font-size:24px;text-align:center;line-height:34px;letter-spacing:-.2px;box-shadow:3px 3px 0 var(--blue-deep)}
.phone{position:absolute;top:52px;left:0;width:100%;display:flex;justify-content:center;align-items:center;gap:8px;color:var(--white);font-weight:800;font-size:37px;letter-spacing:-.5px;line-height:1}
.phone svg{position:static;width:30px;height:30px}
.site{position:absolute;top:92px;width:100%;text-align:center;color:var(--white);font-weight:600;font-size:15px}
/* back */
.hero{position:absolute;left:0;top:0;width:410px;height:440px;background:linear-gradient(180deg,#0d5fb3 0%,#2b83d3 30%,#6fb0e3 55%,#9aa9bd 70%,#7d8a6f 100%)}
.slogan{position:absolute;right:38px;top:82px;text-align:right;color:var(--white);font-weight:800;font-style:italic;font-size:17px;line-height:1.17;z-index:3}
.stat{position:absolute;top:500px;width:150px;text-align:center}
.stat__num{font-size:86px;font-weight:900;color:var(--blue);line-height:.92;letter-spacing:-3px;text-shadow:3px 3px 0 var(--sky)}
.stat__unit{font-size:30px;font-weight:800;color:var(--blue);line-height:1.15;text-shadow:2px 2px 0 var(--sky-pale)}
.stat__label{margin-top:6px;font-size:15px;font-weight:600;color:var(--text);line-height:1.15}
.badges{position:absolute;top:692px;left:0;width:100%}
.badge{position:absolute}
.contact{position:absolute;top:752px;width:100%;text-align:center;color:var(--blue)}
.contact__title{font-size:34px;font-weight:900;letter-spacing:-.5px;line-height:1.1}
.contact__offer{font-size:16px;font-weight:800;color:var(--blue-bright);margin-top:2px}
.contact__fine{font-size:10.5px;font-weight:500;color:var(--ink);margin-top:5px}
</style>
</head>
<body>

<!-- FRONT -->
<section class="hanger hanger--front">
  <svg class="abs" style="left:0;top:0" width="410" height="180" viewBox="0 0 410 180">
    <path d="M0 0H410V128C330 104 250 100 170 114C100 126 50 128 0 122Z" fill="var(--blue)"/>
    <path d="M0 122C50 128 100 126 170 114C250 100 330 104 410 128V172C360 128 270 116 170 124C100 131 50 132 0 130Z" fill="var(--blue-bright)" opacity=".85"/>
  </svg>
  <p class="headline">WE’RE IN YOUR <em>NEIGHBOURHOOD!</em></p>

  <div class="brand">
    <p class="brand__est">Est. 1991</p>
    <p class="brand__name"><span class="brand__mark"></span>PELLMONT</p>
    <p class="brand__sub">ROOFING &amp; SIDING</p>
  </div>

  <div class="service" style="top:383px;height:164px">
    <div class="service__bg"></div>
    <div class="service__photo" role="img" aria-label="Photo of a shingled roof with a dormer window" style="left:170px;top:25px;width:240px;height:127px;clip-path:polygon(6% 0,100% 0,100% 100%,0 100%)"></div>
    <div class="tab" style="width:192px">ROOFING</div>
    <ul class="checklist" style="left:63px;top:60px">
      <li style="margin-bottom:4.5px">Asphalt</li>
      <li style="margin-bottom:4.5px">Cedar Shakes</li>
      <li style="margin-bottom:4.5px">Rubber</li>
      <li>Metal</li>
    </ul>
  </div>

  <div class="service" style="top:549px;height:164px">
    <div class="service__bg"></div>
    <div class="service__photo" role="img" aria-label="Photo of white house siding and roof eaves with gutter" style="left:196px;top:17px;width:214px;height:147px;background:linear-gradient(200deg,#f3f6f9 0%,#d2dae2 50%,#aeb9c4 100%);clip-path:polygon(60% 0,100% 0,100% 100%,10% 100%,0 70%)"></div>
    <div class="tab" style="width:192px">SIDING</div>
    <ul class="checklist" style="left:63px;top:48px">
      <li style="margin-bottom:4px">Owen Brisket fibre cement</li>
      <li style="margin-bottom:4px">Vinyl</li>
      <li style="margin-bottom:4px">Stucco</li>
      <li>Metal<br><span class="note">(Steel, Aluminum)<br>Longboard</span></li>
    </ul>
  </div>

  <div class="service" style="top:714px;height:160px">
    <div class="service__bg"></div>
    <div class="tab" style="width:289px">FULL EXTERIORS</div>
    <ul class="checklist" style="left:63px;top:55px">
      <li style="margin-bottom:6px">Gutter/Soffit/Fascia</li>
      <li style="margin-bottom:6px">Stone</li>
      <li>Skylights</li>
    </ul>
    <ul class="checklist" style="left:237px;top:55px">
      <li style="margin-bottom:6px">Windows &amp; Doors</li>
      <li style="margin-bottom:6px">Insulation</li>
      <li>Painting</li>
    </ul>
  </div>

  <div class="footer">
    <svg viewBox="0 0 410 136" width="410" height="136"><path d="M0 30C120 18 290 14 410 30V136H0Z" fill="var(--blue)"/></svg>
    <div class="cta">FREE ESTIMATES</div>
    <div class="phone"><svg viewBox="0 0 30 30"><circle cx="15" cy="15" r="15" fill="#fff"/><path d="M10.5 7.5l3 3-2 2.2c.9 2 2.6 3.8 4.7 4.7l2.2-2 3 3-2.2 2.5c-5.4-.6-10.8-6-11.3-11.3z" fill="var(--blue)"/></svg>403-555-0148</div>
    <p class="site">www.pellmontshingleworks.com</p>
  </div>
</section>

<!-- BACK -->
<section class="hanger hanger--back">
  <div class="hero" role="img" aria-label="Photo of a two-storey blue-grey house with white trim, garage and front lawn under a clear blue sky"></div>
  <svg class="abs" style="left:0;top:400px" width="410" height="110" viewBox="0 0 410 110">
    <path d="M0 40C110 80 260 10 410 30V110H0Z" fill="#fff"/>
    <path d="M0 32C120 70 260 -2 410 14V40C270 30 140 80 0 68Z" fill="#fff"/>
    <path d="M0 44C120 80 270 10 410 28V60C270 46 130 104 0 80Z" fill="var(--blue)"/>
    <path d="M0 80C130 104 270 46 410 60V76C280 66 140 116 0 94Z" fill="var(--sky)"/>
  </svg>
  <p class="headline">WE’RE IN YOUR <em>NEIGHBOURHOOD!</em></p>
  <p class="slogan">Raised<br>On Care,<br>Proven Through<br>Seasons</p>

  <svg class="abs" style="left:0;top:500px" width="410" height="185" viewBox="0 0 410 185">
    <g fill="none" stroke="var(--blue-bright)" stroke-width="1.3">
      <path d="M199 5V150Q199 178 170 178H48"/>
      <path d="M363 5V150Q363 178 335 178H210"/>
    </g>
    <g fill="var(--blue-bright)"><circle cx="199" cy="5" r="2.2"/><circle cx="48" cy="178" r="2.2"/><circle cx="363" cy="5" r="2.2"/><circle cx="210" cy="178" r="2.2"/></g>
  </svg>
  <div class="stat" style="left:50px">
    <p class="stat__num">25</p>
    <p class="stat__unit">YEARS</p>
    <p class="stat__label">LABOUR<br>WARRANTY'S<br>AVAILABLE</p>
  </div>
  <div class="stat" style="left:215px">
    <p class="stat__num">32</p>
    <p class="stat__unit">YEARS</p>
    <p class="stat__label"><br>IN CALGARY</p>
  </div>

  <div class="badges">
    <div class="badge" role="img" aria-label="NWTG Prairie Joint Shingle Guild member badge" style="left:48px;top:4px;width:52px;height:44px;background:var(--blue);border-radius:4px"></div>
    <div class="badge" role="img" aria-label="QCR A+ rating badge" style="left:124px;top:4px;width:70px;height:40px;background:var(--blue-deep);border-radius:3px"></div>
    <div class="badge" role="img" aria-label="KOV Summit Select badge" style="left:225px;top:0;width:38px;height:44px;background:var(--red)"></div>
    <div class="badge" role="img" aria-label="Owen Brisket partner badge" style="left:297px;top:4px;width:48px;height:40px;border-radius:50%;background:#2e8a3c"></div>
  </div>

  <div class="contact">
    <p class="contact__title">contact us today</p>
    <p class="contact__offer">for your Exclusive limited time offer</p>
    <p class="contact__fine">*discounts apply exclusively to new agreements only</p>
  </div>

  <div class="footer">
    <svg viewBox="0 0 410 136" width="410" height="136"><path d="M0 30C120 18 290 14 410 30V136H0Z" fill="var(--blue)"/></svg>
    <div class="cta">FREE ESTIMATES</div>
    <div class="phone"><svg viewBox="0 0 30 30"><circle cx="15" cy="15" r="15" fill="#fff"/><path d="M10.5 7.5l3 3-2 2.2c.9 2 2.6 3.8 4.7 4.7l2.2-2 3 3-2.2 2.5c-5.4-.6-10.8-6-11.3-11.3z" fill="var(--blue)"/></svg>403-555-0148</div>
    <p class="site">www.pellmontshingleworks.com</p>
  </div>
</section>

</body>
</html>
```